verano habitat

I need a brochure that can help me sell memberships or enrollments into a delivery system for homes of natural products including flower arrangements and also hotel day passes . enclosed are the text and the current logo.

```html
<!DOCTYPE html>
<html lang="es">
<head>
<meta charset="utf-8">
<title>verano habitat — folleto</title>
<link href="https://fonts.googleapis.com/css2?family=Roboto:wght@400;500&display=swap" rel="stylesheet">
<style>
  :root {
    --backdrop: #2a2827;
    --paper: #ffffff;
    --mist: #eceded;
    --mist-deep: #dfe0e1;
    --olive: #a09a2c;
    --olive-dark: #857f17;
    --olive-deep: #6f6a12;
    --band: rgba(255, 255, 255, 0.82);
    --ink: #3a3a3a;
    --sky: #9dbbd2;
    --sea: #5cc3c8;
    --sand: #e3ddd1;
    --foliage: #3f8a3a;
  }
  html, body {
    margin: 0;
    width: 1200px;
    height: 1200px;
    overflow: hidden;
    background: var(--backdrop);
  }
  .canvas {
    width: 1200px;
    height: 1200px;
    display: flex;
    align-items: center;
    justify-content: center;
  }
  .brochure-cover {
    display: block;
    width: 866px;
    height: 1120px;
    box-shadow: 0 20px 50px rgba(0, 0, 0, 0.5);
  }
  .brand-name {
    font-family: "Roboto", sans-serif;
    font-weight: 400;
    font-size: 34px;
    fill: var(--ink);
  }
  .address-line {
    font-family: "Roboto", sans-serif;
    font-weight: 400;
    font-size: 22px;
    fill: var(--ink);
    letter-spacing: 0.2px;
  }
</style>
</head>
<body>
<main class="canvas">
  <svg class="brochure-cover" viewBox="0 0 988 1278" xmlns="http://www.w3.org/2000/svg">
    <defs>
      <linearGradient id="beach-tones" x1="0" y1="0" x2="0" y2="1">
        <stop offset="0" stop-color="var(--sky)"/>
        <stop offset="0.24" stop-color="#a9c6d8"/>
        <stop offset="0.26" stop-color="var(--sea)"/>
        <stop offset="0.31" stop-color="var(--sand)"/>
        <stop offset="0.72" stop-color="#d8d1c3"/>
        <stop offset="0.8" stop-color="var(--foliage)"/>
        <stop offset="1" stop-color="#2f6f2d"/>
      </linearGradient>
    </defs>

    <!-- right panel -->
    <rect class="panel-paper" x="454" y="0" width="534" height="1278" fill="var(--paper)"/>
    <g class="panel-swooshes">
      <path d="M560 0 C700 250 640 560 454 820 L454 700 C590 500 620 260 520 0 Z" fill="var(--mist)"/>
      <path d="M454 900 C640 840 760 720 840 560 L850 600 C760 790 620 900 454 960 Z" fill="var(--mist)"/>
      <path d="M454 1070 C620 1040 780 1040 920 1060 L920 1080 C780 1070 620 1080 454 1110 Z" fill="var(--mist-deep)" opacity="0.6"/>
      <path d="M454 1180 C620 1150 780 1150 900 1160 L900 1278 L454 1278 Z" fill="var(--mist)" opacity="0.5"/>
    </g>
    <g class="panel-chevron">
      <polygon points="918,0 988,0 988,1278 928,1278 690,700" fill="var(--olive-deep)"/>
      <polygon points="936,0 988,0 988,1278 944,1278 714,700" fill="var(--olive-dark)"/>
      <polygon points="962,0 988,0 988,1278 968,1278 742,700" fill="var(--olive)"/>
    </g>
    <rect class="title-band" x="454" y="447" width="534" height="326" fill="var(--band)"/>

    <!-- photo -->
    <rect class="cover-photo" x="0" y="0" width="454" height="1278" fill="url(#beach-tones)"
          role="img" aria-label="Fotografía de playa con palapas de paja, camastros azules, mar turquesa y vegetación en primer plano"/>

    <!-- brand -->
    <g class="brand-lockup">
      <circle cx="640" cy="540" r="22" fill="var(--olive)"/>
      <text class="brand-name" x="674" y="552">verano habitat</text>
    </g>
    <g class="address" text-anchor="middle">
      <text class="address-line" x="719" y="640">AV. PALMA AZUL 48, SMZ. 7, CANCUN,</text>
      <text class="address-line" x="719" y="669">QUINTANA ROO, CP. 77500. TEL.</text>
      <text class="address-line" x="719" y="698">9981.40.22.67</text>
    </g>
  </svg>
</main>
</body>
</html>
```